FLYER für Fortbildung
Zielgruppe
Die Fortbildung, die beworben werden soll, richtet sich an Fachkräfte, die in Kitas arbeiten. In diesem Fall handelt es sich um eine praxisorientierte Online-Live-Fortbildung - dies bedeutet, die TeilnehmerInnen werden während der Online-Fortbildung kontinuierlich durch eine Referentin begleitet. Die Fortbildung erweitert das Wissen und die Kompetenzen der Teilnehmenden.
Aufgabenstellung
Ich freue mich über Vorschläge eines Falzflyers im Format DIN lang. Wie viele Seiten der Flyer umfasst, überlasse ich gerne Ihnen, da dies von Ihrer Gestaltung abhängt.
Falls Sie 1-4 Bilder einfügen möchten, gebe ich Ihnen in den Datei-Upload gerne einige Beispiele, die mir zusagen (zur Auswahl). Darüber hinaus bin ich selbstverständlich auch offen für alternative Vorschläge sowie neue Designs.

```html
<!DOCTYPE html>
<html lang="de">
<head>
<meta charset="utf-8">
<title>Falzflyer – Elterngespräche führen</title>
<link href="https://fonts.googleapis.com/css2?family=Montserrat:wght@700;800;900&family=Poppins:ital,wght@0,400;0,500;0,600;0,700;1,400&display=swap" rel="stylesheet">
<style>
  :root{
    --blue:#5f7896;
    --blue-dark:#4d6482;
    --gold:#b08a55;
    --gold-light:#c9a56e;
    --ink:#1d1d1f;
    --paper:#ffffff;
    --mist:#e9eef4;
    --backdrop:#e4e4e4;
  }
  *{box-sizing:border-box;margin:0;padding:0}
  html,body{width:838px;height:1200px;overflow:hidden;background:var(--backdrop)}
  body{font-family:"Poppins",sans-serif;color:var(--ink);position:relative}
  .spread{position:absolute;left:19px;width:800px;height:566px;overflow:hidden;background:var(--paper);box-shadow:0 4px 14px rgba(0,0,0,.18)}
  .spread--outside{top:22px}
  .spread--inside{top:612px}
  .spread__shapes{position:absolute;inset:0;width:800px;height:566px}
  .photo-slot{position:absolute}

  /* outside – back panel */
  .impressum{position:absolute;left:55px;top:378px;color:#fff}
  .impressum__title{font-size:25px;font-weight:600;letter-spacing:.2px}
  .impressum__rule{width:215px;height:1px;background:rgba(255,255,255,.7);margin:4px 0 12px}
  .impressum__list{list-style:none}
  .impressum__item{display:flex;align-items:center;gap:8px;font-size:17px;font-weight:500;line-height:26px}
  .impressum__item svg{width:13px;height:13px;flex:none}

  /* outside – cover */
  .brand{position:absolute;left:555px;top:38px;display:flex;align-items:center;gap:6px}
  .brand__dot{width:14px;height:14px;border-radius:50%;background:var(--blue)}
  .brand__name{font-size:11px;font-weight:500;color:var(--blue);letter-spacing:.5px}
  .cover-title{position:absolute;left:485px;width:315px;top:362px;text-align:center}
  .cover-title__main{font-family:"Montserrat",sans-serif;font-weight:900;font-size:27px;line-height:30px;color:var(--ink)}
  .cover-title__accent{font-family:"Montserrat",sans-serif;font-weight:800;font-size:27px;line-height:32px;color:var(--blue)}
  .cover-title__sub{font-size:17px;line-height:20px;margin-top:4px}
  .date-pill{display:inline-block;margin-top:8px;background:var(--blue);color:#fff;font-size:9.5px;font-weight:600;padding:3px 9px}

  /* inside – left */
  .intro{position:absolute;left:40px;top:207px;width:330px;font-size:11.5px;line-height:15px}
  .topics{position:absolute;left:40px;top:300px;width:325px;height:128px;border-radius:10px;background:linear-gradient(135deg,var(--gold-light),var(--gold));padding:10px 14px;list-style:none;color:#fff}
  .topics__item{display:flex;align-items:center;gap:7px;font-size:11px;font-weight:600;line-height:18px}
  .topics__item svg{width:10px;height:10px;flex:none}
  .benefit{position:absolute;left:40px;top:446px;width:340px;font-size:11.5px;line-height:14px;font-style:italic;color:#e8eef6}
  .fee{position:absolute;left:40px;top:496px;font-size:16px;font-weight:600;color:#fff}
  .fee-note{position:absolute;left:40px;top:521px;font-size:7px;font-style:italic;color:#dbe3ec}

  /* inside – registration */
  .form-card{position:absolute;left:419px;top:8px;width:366px;height:540px;background:var(--paper);padding:24px 18px 0 18px}
  .form-card__title{font-size:14px;font-weight:700;color:var(--gold);letter-spacing:.3px}
  .form-card__course{font-size:8.5px;font-weight:600;margin-top:16px}
  .form-card__when{font-size:7px;margin-top:2px}
  .field{display:flex;align-items:flex-end;gap:4px;font-size:7px;font-weight:600;margin-top:14px}
  .field__line{flex:1;border-bottom:1px solid #777;height:9px}
  .blank-line{border-bottom:1px solid #999;height:14px}
  .notes{margin-top:30px;font-size:7px;line-height:9px;color:#333}
  .notes__title{font-size:10.5px;font-weight:600;color:var(--blue);margin-bottom:3px}
  .notes p{margin-bottom:8px}
  .signatures{position:absolute;left:18px;right:18px;bottom:16px;display:flex;gap:22px}
  .signatures__slot{flex:1;border-top:1px solid #555;text-align:center;font-size:7px;padding-top:3px}
</style>
</head>
<body>

<!-- Outside spread: back panel + cover -->
<section class="spread spread--outside" aria-label="Außenseite des Flyers">
  <svg class="spread__shapes" viewBox="0 0 800 566" aria-hidden="true">
    <defs>
      <linearGradient id="goldSwoosh" x1="0" y1="0" x2="0" y2="1">
        <stop offset="0" stop-color="#8a6a3c"/><stop offset=".5" stop-color="#d8b67e"/><stop offset="1" stop-color="#9c7843"/>
      </linearGradient>
    </defs>
    <path d="M0 365 C150 335 300 350 470 400 L470 566 L0 566 Z" fill="var(--blue)"/>
    <path d="M425 0 C395 200 430 420 470 566 L800 566 L800 0 Z" fill="#fff"/>
    <path d="M425 0 C395 200 430 420 470 566" fill="none" stroke="url(#goldSwoosh)" stroke-width="12"/>
    <path d="M440 0 C418 180 470 360 520 440" fill="none" stroke="url(#goldSwoosh)" stroke-width="3"/>
  </svg>

  <svg class="photo-slot" style="left:0;top:0" width="440" height="400" viewBox="0 0 440 400" role="img" aria-label="Foto: lächelnde Beraterin am Schreibtisch in hellem Büro">
    <defs><linearGradient id="backPhoto" x1="0" y1="0" x2="1" y2="1"><stop offset="0" stop-color="#eef0f1"/><stop offset=".55" stop-color="#c9b4a0"/><stop offset="1" stop-color="#9fa9b3"/></linearGradient></defs>
    <path d="M0 0 H428 C402 150 405 300 420 400 C300 350 150 340 0 368 Z" fill="url(#backPhoto)"/>
  </svg>

  <svg class="photo-slot" style="left:430px;top:0" width="370" height="440" viewBox="0 0 370 440" role="img" aria-label="Foto: Erzieherin spielt mit einem Kind in der Kita">
    <defs><linearGradient id="coverPhoto" x1="0" y1="0" x2="1" y2="1"><stop offset="0" stop-color="#d7cfc2"/><stop offset=".5" stop-color="#c8a36d"/><stop offset="1" stop-color="#5b6a80"/></linearGradient></defs>
    <path d="M14 0 H370 V325 C290 335 200 355 135 425 C60 330 -10 180 14 0 Z" fill="url(#coverPhoto)"/>
  </svg>

  <svg class="photo-slot" style="left:630px;top:195px" width="120" height="120" viewBox="0 0 120 120" role="img" aria-label="Rundes Foto: Referentin vor dem Laptop">
    <circle cx="60" cy="60" r="56" fill="#fff"/>
    <circle cx="60" cy="60" r="50" fill="#b7c2cf" stroke="var(--blue)" stroke-width="5"/>
  </svg>

  <div class="brand"><span class="brand__dot"></span><span class="brand__name">GELASSEN IM BERUF</span></div>

  <div class="impressum">
    <h2 class="impressum__title">Impressum</h2>
    <div class="impressum__rule"></div>
    <ul class="impressum__list">
      <li class="impressum__item"><svg viewBox="0 0 24 24"><path fill="#fff" d="M6.6 10.8a15 15 0 0 0 6.6 6.6l2.2-2.2c.3-.3.7-.4 1-.2 1.1.4 2.3.6 3.6.6.6 0 1 .4 1 1V20c0 .6-.4 1-1 1A17 17 0 0 1 3 4c0-.6.4-1 1-1h3.5c.6 0 1 .4 1 1 0 1.3.2 2.5.6 3.6.1.3 0 .7-.2 1z"/></svg>0123-456-789</li>
      <li class="impressum__item"><svg viewBox="0 0 24 24"><circle cx="12" cy="12" r="10" fill="#fff"/><path d="M2 12h20M12 2c3 3 3 17 0 20M12 2c-3 3-3 17 0 20" stroke="var(--blue)" stroke-width="1.6" fill="none"/></svg>www.gelassenimberuf.com</li>
      <li class="impressum__item"><svg viewBox="0 0 24 24"><circle cx="12" cy="12" r="10" fill="#fff"/><path d="M7 9h10v7H7zM7 9l5 4 5-4" stroke="var(--blue)" stroke-width="1.5" fill="none"/></svg>info@gelassen-im-beruf.de</li>
      <li class="impressum__item"><svg viewBox="0 0 24 24"><path fill="#fff" d="M12 2a7 7 0 0 0-7 7c0 5 7 13 7 13s7-8 7-13a7 7 0 0 0-7-7zm0 9.5A2.5 2.5 0 1 1 12 6.5a2.5 2.5 0 0 1 0 5z"/></svg>Lindenweg 12, Musterstadt</li>
    </ul>
  </div>

  <div class="cover-title">
    <h1 class="cover-title__main">ELTERNGESPRÄCHE<br>FÜHREN –</h1>
    <div class="cover-title__accent">GRUNDLAGEN</div>
    <p class="cover-title__sub">Live-Online-Fortbildung für<br>Mitarbeitende in Kitas</p>
    <span class="date-pill">Montag, den 30. März 2026 &nbsp;|&nbsp; 09:00 bis 15:00 Uhr</span>
  </div>
</section>

<!-- Inside spread: information + registration -->
<section class="spread spread--inside" aria-label="Innenseite des Flyers">
  <svg class="spread__shapes" viewBox="0 0 800 566" aria-hidden="true">
    <rect x="400" y="0" width="400" height="566" fill="var(--mist)"/>
    <rect x="400" y="330" width="400" height="236" fill="var(--blue)"/>
    <path d="M0 400 C140 380 290 350 400 335 L400 566 L0 566 Z" fill="var(--blue)"/>
  </svg>

  <svg class="photo-slot" style="left:0;top:0" width="400" height="200" viewBox="0 0 400 200" role="img" aria-label="Foto: Beraterin im Gespräch mit Eltern am Tisch">
    <defs><linearGradient id="insidePhoto" x1="0" y1="0" x2="1" y2="0"><stop offset="0" stop-color="#4a5668"/><stop offset=".45" stop-color="#e5e4e0"/><stop offset="1" stop-color="#6f7680"/></linearGradient></defs>
    <path d="M0 0 H400 V130 C300 120 230 140 170 160 C110 180 50 185 0 195 Z" fill="url(#insidePhoto)"/>
  </svg>

  <p class="intro">Diese Fortbildung richtet sich an Berufsanfänger, unsichere Fachkräfte und alle, die ihre Kenntnisse bezüglich Elterngesprächen auffrischen möchten. Ziel ist es, Ihnen Sicherheit und Selbstvertrauen im Umgang mit Eltern zu geben. Benötigt wird ein PC oder Laptop mit Webcam/Mikrofon.</p>

  <ul class="topics">
    <li class="topics__item"><svg viewBox="0 0 10 10"><circle cx="5" cy="5" r="5" fill="#fff"/><path d="M2.8 5.2l1.5 1.4 2.9-3" stroke="var(--gold)" stroke-width="1.3" fill="none"/></svg>Theoretische Modelle der Gesprächsführung</li>
    <li class="topics__item"><svg viewBox="0 0 10 10"><circle cx="5" cy="5" r="5" fill="#fff"/><path d="M2.8 5.2l1.5 1.4 2.9-3" stroke="var(--gold)" stroke-width="1.3" fill="none"/></svg>Effektive Vorbereitung auf Elterngespräche</li>
    <li class="topics__item"><svg viewBox="0 0 10 10"><circle cx="5" cy="5" r="5" fill="#fff"/><path d="M2.8 5.2l1.5 1.4 2.9-3" stroke="var(--gold)" stroke-width="1.3" fill="none"/></svg>Gesprächseinstieg</li>
    <li class="topics__item"><svg viewBox="0 0 10 10"><circle cx="5" cy="5" r="5" fill="#fff"/><path d="M2.8 5.2l1.5 1.4 2.9-3" stroke="var(--gold)" stroke-width="1.3" fill="none"/></svg>Umgang mit schwierigen Gesprächssituationen</li>
    <li class="topics__item"><svg viewBox="0 0 10 10"><circle cx="5" cy="5" r="5" fill="#fff"/><path d="M2.8 5.2l1.5 1.4 2.9-3" stroke="var(--gold)" stroke-width="1.3" fill="none"/></svg>Deeskalation / Konfliktlösungsstrategien</li>
    <li class="topics__item"><svg viewBox="0 0 10 10"><circle cx="5" cy="5" r="5" fill="#fff"/><path d="M2.8 5.2l1.5 1.4 2.9-3" stroke="var(--gold)" stroke-width="1.3" fill="none"/></svg>Möglichkeiten zum Üben und Austausch</li>
  </ul>

  <p class="benefit">Profitieren Sie von praxisnahen Tipps und Übungen, die Ihnen helfen, Ihre Kommunikationsfähigkeiten zu stärken und schwierige Situationen souverän zu meistern.</p>
  <p class="fee">Teilnahmegebühr: 99,00 € pro Person</p>
  <p class="fee-note">*gemäß § 19 UstG Kleinunternehmerregelung, daher ohne Mehrwertsteuer.</p>

  <div class="form-card">
    <h2 class="form-card__title">ANMELDUNG ZUR FORTBILDUNG</h2>
    <p class="form-card__course">Elterngespräche führen – Grundlagen</p>
    <p class="form-card__when">am 30. März 2025 von 09:00 – 15:00 Uhr (online)</p>
    <div class="field">Vor- und Zuname:<span class="field__line"></span></div>
    <div class="field">Rechnungsadresse:<span class="field__line"></span></div>
    <div class="blank-line"></div>
    <div class="blank-line"></div>
    <div class="blank-line"></div>
    <div class="blank-line"></div>
    <div class="field" style="margin-top:26px">Ihre E-Mail-Adresse für den Zugangslink:</div>
    <div class="blank-line"></div>
    <div class="notes">
      <h3 class="notes__title">Hinweise:</h3>
      <p>Bitte füllen Sie das Formular aus und senden Sie es an info@gelassen-im-beruf.de</p>
      <p>Sobald uns Ihre Anmeldung vorliegt, erhalten Sie die Zahlungsinformationen. Die Teilnahmegebühr beträgt 99,00 € pro Person. Bitte beachten Sie, dass Plätze, für die keine Zahlungen geleistet werden, an andere Interessierte weitergegeben werden.</p>
      <p>Der Zugangslink wird Ihnen eine Woche vor Beginn der Veranstaltung zugesandt.</p>
      <p>Mit Ihrer Anmeldung erklären Sie sich mit unseren AGB einverstanden. Sie stimmen außerdem zu, dass wir Ihre personenbezogenen Daten, darunter Name, E-Mail-Adresse sowie Datum und Titel der besuchten Veranstaltung verwenden. Zudem stimmen Sie zu, dass wir Sie über interessante Fortbildungsangebote informieren dürfen. Diese Zustimmung können Sie jederzeit widerrufen.</p>
    </div>
    <div class="signatures">
      <span class="signatures__slot">Ort, Datum</span>
      <span class="signatures__slot">Unterschrift</span>
    </div>
  </div>
</section>

</body>
</html>
```